2014 Orvana Globe Series Contest 1 - Photoshop Tavo Diving

The 2014 Orvana Globe Series got off to a typically theatrical start with Brazil scoring Croatia an 'own goal' and Brazilian player, Tavo, landing 'Dive of the Day' in a refereeing controversy in the 69th minute. Quickly thereafter Brazil secured a 3-1 victory over Croatia. The game captivated a global audience with on-field drama encompassing thrills, spills and heroic player dives - and it's the latter we're highlighting in this fun community design contest.

Designers are invited to photoshop an image capturing Brazilian player, Tavo's famous dive with signs and objects to produce a humorous graphic of Tavo's dive of the day.

It's up to you what elements you want to include alongside Tavo's Famous Dive. Tavo could appear as the figure slipping on public signage or the signage could be featured on the pitch - you decide! Some ideas include funny signs, famous places, and the placement of objects/people/animals in funny places.

A few public signage ideas include: "Caution: Slippery When Wet"; "Caution: Slippery When Dry"; "Stop"; "Walk Don't Run"; "Children's Crossing"; "Please Keep Off The Grass"; "Slow - Children Playing", "No Trespassing" etc etc

Check out images of 'public signage' online including the caution / instructional signs above. There's a whole world of weird and wonderful public safety signs out there so enjoy!

And, if Sulky Moth makes an appearance in your design, we won't be upset - anything goes!

Replay Tavo's Famous Dive here: http://www.quillpost.example/blogs/the_nook/2014/06/12/brazil_s_tavo_gets_the_dive_of_the_day_and_it_might_be_the_dive_of_the_tournament.html

This contest is sponsored by MakerHive and is not endorsed by GLOMA.

Have fun!

```html
<!DOCTYPE html>
<html lang="en">
<head>
<meta charset="utf-8">
<title>Caution – Slippery When Near Goal</title>
<link rel="stylesheet" href="https://fonts.googleapis.com/css2?family=Stardos+Stencil:wght@700&family=Roboto+Condensed:wght@700&display=swap">
<style>
  :root {
    --sign-yellow: #ffe400;
    --sign-black: #0d0d0d;
    --pictogram-tone: #e3c800;
  }
  html, body {
    margin: 0;
    padding: 0;
    width: 1200px;
    height: 857px;
    overflow: hidden;
    background: var(--sign-yellow);
  }
  .sign {
    position: relative;
    width: 1200px;
    height: 857px;
    background: var(--sign-yellow);
  }
  .sign-frame {
    position: absolute;
    left: 17px;
    top: 17px;
    width: 1166px;
    height: 823px;
    box-sizing: border-box;
    border: 17px solid var(--sign-black);
    border-radius: 34px;
  }
  .sign-header {
    position: absolute;
    left: 65px;
    top: 51px;
    width: 1070px;
    height: 166px;
    background: var(--sign-black);
    border-radius: 17px;
    display: flex;
    align-items: center;
    justify-content: center;
  }
  .sign-title {
    margin: 0;
    font-family: "Stardos Stencil", "Black Ops One", sans-serif;
    font-weight: 700;
    font-size: 152px;
    line-height: 1;
    letter-spacing: 0.09em;
    padding-left: 0.09em;
    color: var(--sign-yellow);
    transform: translateY(6px);
  }
  .falling-figure {
    position: absolute;
    left: 146px;
    top: 326px;
    width: 330px;
    height: 380px;
    background: var(--pictogram-tone);
    border-radius: 12px;
  }
  .sign-message {
    position: absolute;
    left: 590px;
    top: 330px;
    width: 570px;
    margin: 0;
    font-family: "Roboto Condensed", "Arial Narrow", sans-serif;
    font-weight: 700;
    font-size: 108px;
    line-height: 116px;
    letter-spacing: 0.02em;
    text-align: center;
    color: var(--sign-black);
  }
  .sign-message span {
    display: block;
  }
</style>
</head>
<body>
  <main class="sign">
    <div class="sign-frame"></div>
    <header class="sign-header">
      <h1 class="sign-title">CAUTION</h1>
    </header>
    <div class="falling-figure" role="img" aria-label="Pictogram of a person slipping and falling backwards"></div>
    <p class="sign-message">
      <span>SLIPPERY</span>
      <span>WHEN</span>
      <span>NEAR GOAL</span>
    </p>
  </main>
</body>
</html>
```